Real estate investor, needing a business card that communicates warmth, integrity, empathy.

I have a logo that can be manipulated to align with the message - "Serving your home selling needs." Want it to stand out from typical real estate investor cards, and make distressed home sellers feel a connection with me. Should communicate warmth, integrity, empathy, and trustworthiness.

Target Market(s)

Distressed home owners who need to sell their homes, not using realtors.

Contact Information for Business Card

Glossy front and matte back, with a small box that is labelled "notes." I like darker blues and blacks together, but doesn't have to be, as long as it communicates trustworthiness, and a strong call to action.

Other font styles liked:
• see "must haves" above, but willing to review whatever comes my way.

Requirements
Must have
• The fonts on my logo are Aviano, Lusitana, and Marcellus. We don't have to use those, but I favor them.

```html
<!DOCTYPE html>
<html lang="en">
<head>
<meta charset="utf-8">
<title>Ridgeline Home Buyers – Business Card</title>
<link href="https://fonts.googleapis.com/css2?family=Lusitana:wght@400;700&family=Raleway:wght@300;400&display=swap" rel="stylesheet">
<style>
  :root {
    --backdrop: #e9e4db;
    --card-top: #2b2b2b;
    --card-bottom: #141414;
    --ink: #ffffff;
    --ink-soft: #d9d9d9;
    --gold: #b8946a;
    --shadow: rgba(0, 0, 0, 0.35);
  }
  * { box-sizing: border-box; margin: 0; padding: 0; }
  html, body {
    width: 771px;
    height: 1200px;
    overflow: hidden;
    background: var(--backdrop);
  }
  .canvas {
    position: relative;
    width: 771px;
    height: 1200px;
  }
  .card {
    position: absolute;
    left: 55px;
    width: 661px;
    height: 378px;
    border-radius: 6px;
    background: linear-gradient(160deg, var(--card-top) 0%, var(--card-bottom) 70%);
    box-shadow: 0 18px 40px var(--shadow);
    overflow: hidden;
    color: var(--ink);
  }
  .card--front { top: 160px; }
  .card--back { top: 662px; }

  /* brand name (set in the piece's own serif) */
  .brand {
    font-family: "Lusitana", Georgia, serif;
    font-weight: 700;
    color: var(--ink);
    letter-spacing: 0.04em;
    display: flex;
    align-items: center;
    gap: 12px;
  }
  .brand__square {
    width: 14px;
    height: 14px;
    background: var(--gold);
  }
  .tagline {
    font-family: "Lusitana", Georgia, serif;
    font-weight: 700;
  }

  /* front */
  .front__brand {
    position: absolute;
    top: 46px;
    right: 44px;
    font-size: 30px;
  }
  .front__tagline {
    position: absolute;
    top: 100px;
    right: 44px;
    font-size: 16px;
    color: var(--ink-soft);
  }
  .identity {
    position: absolute;
    left: 44px;
    top: 168px;
    padding-left: 18px;
    border-left: 2px solid var(--gold);
    font-family: "Raleway", Arial, sans-serif;
    font-weight: 300;
  }
  .identity__name {
    font-size: 34px;
    letter-spacing: 0.06em;
    color: var(--ink);
  }
  .identity__title {
    margin-top: 6px;
    font-size: 16px;
    letter-spacing: 0.14em;
    color: var(--gold);
  }
  .front__rule {
    position: absolute;
    left: 44px;
    right: 44px;
    top: 272px;
    height: 1px;
    background: var(--gold);
  }
  .contacts {
    position: absolute;
    left: 44px;
    right: 44px;
    top: 298px;
    display: flex;
    justify-content: space-between;
    list-style: none;
    font-family: "Raleway", Arial, sans-serif;
    font-weight: 400;
    font-size: 15px;
    color: var(--ink-soft);
  }
  .contacts__item {
    display: flex;
    align-items: center;
    gap: 9px;
  }
  .contacts__icon {
    width: 14px;
    height: 14px;
    fill: var(--gold);
  }

  /* back */
  .back__content {
    position: absolute;
    inset: 0;
    display: flex;
    flex-direction: column;
    align-items: center;
    justify-content: center;
  }
  .back__brand { font-size: 40px; }
  .back__tagline {
    margin-top: 20px;
    padding-bottom: 8px;
    border-bottom: 1px solid var(--gold);
    font-size: 17px;
    color: var(--gold);
  }
</style>
</head>
<body>
<main class="canvas">

  <section class="card card--front" aria-label="Card front">
    <div class="brand front__brand">
      <span class="brand__square"></span>
      <span>Ridgeline Home Buyers</span>
    </div>
    <p class="tagline front__tagline">Serving Your home selling Needs</p>

    <div class="identity">
      <p class="identity__name">YOUR NAME</p>
      <p class="identity__title">JOB TITLE</p>
    </div>

    <div class="front__rule"></div>

    <ul class="contacts">
      <li class="contacts__item">
        <svg class="contacts__icon" viewBox="0 0 24 24" aria-hidden="true"><path d="M6.6 10.8a15.1 15.1 0 0 0 6.6 6.6l2.2-2.2a1 1 0 0 1 1-.25 11.4 11.4 0 0 0 3.6.57 1 1 0 0 1 1 1V20a1 1 0 0 1-1 1A17 17 0 0 1 3 4a1 1 0 0 1 1-1h3.5a1 1 0 0 1 1 1 11.4 11.4 0 0 0 .57 3.6 1 1 0 0 1-.25 1z"/></svg>
        <span>000 000 0000</span>
      </li>
      <li class="contacts__item">
        <svg class="contacts__icon" viewBox="0 0 24 24" aria-hidden="true"><path d="M2 5h20v14H2z M2 5l10 8 10-8" fill="none" stroke="var(--gold)" stroke-width="2"/></svg>
        <span>youremail@xyz.com</span>
      </li>
      <li class="contacts__item">
        <svg class="contacts__icon" viewBox="0 0 24 24" aria-hidden="true"><circle cx="12" cy="12" r="10" fill="none" stroke="var(--gold)" stroke-width="2"/><path d="M2 12h20M12 2c3 3 3 17 0 20M12 2c-3 3-3 17 0 20" fill="none" stroke="var(--gold)" stroke-width="1.6"/></svg>
        <span>www.yourwebsite.com</span>
      </li>
    </ul>
  </section>

  <section class="card card--back" aria-label="Card back">
    <div class="back__content">
      <div class="brand back__brand">
        <span class="brand__square"></span>
        <span>Ridgeline Home Buyers</span>
      </div>
      <p class="tagline back__tagline">Serving Your home selling Needs</p>
    </div>
  </section>

</main>
</body>
</html>
```